Up to the Challenge - PPT Template with Splash Slide

We are looking for a PPT template that has 4 slides.
1. Splash slide (Creative, fun, no content, a visual representation of the theme)
2. Section header slide
3. Content Slide
4. Content Slide, another design option
The theme is 'UP to the Challenge'. The design should reflect this theme.
The colors should be in Purple (#864B99), Blue (#0A80C2), and Green (#52B054).

```html
<!DOCTYPE html>
<html lang="en">
<head>
<meta charset="utf-8">
<title>Up to the Challenge – Slide Template</title>
<link rel="stylesheet" href="https://fonts.googleapis.com/css2?family=Red+Hat+Display:wght@300;400;500;600;900&family=Yellowtail&display=swap">
<style>
  :root {
    --purple: #864B99;
    --blue: #0A80C2;
    --green: #52B054;
    --ink: #151515;
    --ink-soft: #3a3a3a;
    --paper: #ffffff;
    --backdrop: #8aa9d4;
  }
  html, body {
    margin: 0;
    padding: 0;
    width: 1200px;
    height: 737px;
    overflow: hidden;
    background: var(--backdrop);
  }
  .deck {
    position: relative;
    width: 1200px;
    height: 737px;
  }
  .slide {
    position: absolute;
    width: 538px;
    height: 303px;
    display: block;
    background: var(--paper);
  }
  .slide--splash   { left: 50px;  top: 54px; }
  .slide--section  { left: 611px; top: 54px; }
  .slide--content-a{ left: 50px;  top: 379px; }
  .slide--content-b{ left: 611px; top: 379px; }

  .shape-purple { fill: var(--purple); }
  .shape-blue   { fill: var(--blue); }
  .shape-green  { fill: var(--green); }

  .script-title {
    font-family: "Yellowtail", cursive;
    fill: var(--ink-soft);
  }
  .caps-title {
    font-family: "Red Hat Display", sans-serif;
    font-weight: 900;
  }
  .caps-title--purple { fill: var(--purple); }
  .caps-title--ink { fill: var(--ink); }
  .lead-text {
    font-family: "Red Hat Display", sans-serif;
    font-weight: 500;
    fill: var(--ink);
  }
  .body-text {
    font-family: "Red Hat Display", sans-serif;
    font-weight: 300;
    fill: var(--ink-soft);
  }
  .subtitle-text {
    font-family: "Red Hat Display", sans-serif;
    font-weight: 400;
    fill: var(--ink-soft);
  }
  .photo-frame--purple { stroke: var(--purple); }
  .photo-frame--green  { stroke: var(--green); }
  .photo-frame--blue   { stroke: var(--blue); }
</style>
</head>
<body>
<main class="deck">

  <!-- Splash slide -->
  <svg class="slide slide--splash" viewBox="0 0 1107 623" xmlns="http://www.w3.org/2000/svg">
    <defs>
      <linearGradient id="climb-tone" x1="0" y1="0" x2="0.3" y2="1">
        <stop offset="0" stop-color="#eeeeee"/>
        <stop offset="0.3" stop-color="#6d6055"/>
        <stop offset="0.7" stop-color="#5a4c43"/>
        <stop offset="1" stop-color="#c79aa0"/>
      </linearGradient>
    </defs>
    <rect width="1107" height="623" fill="#f3f3f3"/>
    <rect width="1107" height="623" fill="url(#climb-tone)" role="img" aria-label="Photo of a young girl in a harness climbing an indoor rock wall"/>
    <path class="shape-purple" d="M0,0 L455,0 C462,90 430,170 360,215 C300,250 230,240 170,215 C110,190 50,165 0,160 Z"/>
    <path class="shape-green" d="M0,205 C70,178 200,180 280,255 C350,330 335,500 390,623 L0,623 Z"/>
    <path class="shape-green" d="M640,623 C700,545 800,495 880,508 C940,520 975,585 985,623 Z"/>
    <path class="shape-blue" d="M470,0 C505,75 580,108 640,90 C685,75 712,30 740,0 Z"/>
    <path class="shape-blue" d="M915,0 C950,60 962,180 1010,258 C1042,308 1080,335 1107,342 L1107,0 Z"/>
  </svg>

  <!-- Section header slide -->
  <svg class="slide slide--section" viewBox="0 0 1107 623" xmlns="http://www.w3.org/2000/svg">
    <rect width="1107" height="623" fill="var(--paper)"/>
    <path class="shape-blue" d="M0,0 L238,0 C252,62 228,120 170,160 C112,198 52,208 0,210 Z"/>
    <path class="shape-green" d="M990,0 C960,40 968,100 1010,160 C1060,230 1120,290 1092,360 C1062,420 932,430 852,442 C752,458 680,530 670,623 L1107,623 L1107,0 Z"/>
    <path class="shape-purple" d="M35,623 C50,560 110,517 180,517 C250,517 315,560 325,623 Z"/>
    <text class="script-title" x="216" y="322" font-size="122">Section</text>
    <text class="caps-title caps-title--purple" x="220" y="403" font-size="78">HEADER</text>
    <text class="subtitle-text" x="584" y="262" font-size="37">Lorem Ipsum</text>
    <text class="subtitle-text" x="584" y="308" font-size="37">dolor sit</text>
    <text class="subtitle-text" x="584" y="357" font-size="33">Lorem Ipsum dolor sit</text>
    <text class="subtitle-text" x="584" y="395" font-size="33">Lorem Ipsum dolor</text>
  </svg>

  <!-- Content slide A -->
  <svg class="slide slide--content-a" viewBox="0 0 1107 623" xmlns="http://www.w3.org/2000/svg">
    <defs>
      <linearGradient id="audience-tone" x1="0" y1="0" x2="0" y2="1">
        <stop offset="0" stop-color="#4f5667"/>
        <stop offset="1" stop-color="#2b2622"/>
      </linearGradient>
      <linearGradient id="hall-tone" x1="0" y1="0" x2="0" y2="1">
        <stop offset="0" stop-color="#6b5a55"/>
        <stop offset="1" stop-color="#1f2330"/>
      </linearGradient>
      <radialGradient id="globe-tone" cx="0.4" cy="0.35" r="0.7">
        <stop offset="0" stop-color="#6f9bb8"/>
        <stop offset="0.6" stop-color="#2f5d7d"/>
        <stop offset="1" stop-color="#16324a"/>
      </radialGradient>
    </defs>
    <rect width="1107" height="623" fill="var(--paper)"/>
    <path class="shape-blue" d="M330,0 L1107,0 L1107,623 L523,623 C540,560 570,500 600,470 L620,150 C520,140 420,120 370,80 C345,60 330,30 330,0 Z"/>
    <circle class="shape-green" cx="355" cy="81" r="54"/>
    <rect class="photo-frame--purple" x="592" y="70" width="347" height="313" rx="16" fill="url(#audience-tone)" stroke-width="8" role="img" aria-label="Photo of an audience watching a speaker on stage"/>
    <rect class="photo-frame--green" x="787" y="348" width="252" height="227" rx="16" fill="url(#hall-tone)" stroke-width="8" role="img" aria-label="Photo of a seated audience in a conference hall"/>
    <circle cx="653" cy="501" r="98" fill="url(#globe-tone)" role="img" aria-label="Illustration of planet Earth"/>
    <text class="script-title" x="63" y="134" font-size="96">Slide</text>
    <text class="caps-title caps-title--purple" x="65" y="193" font-size="54">HEADING</text>
    <text class="lead-text" font-size="23">
      <tspan x="65" y="266">Lorem ipsum dolor sit amet, consectetur</tspan>
      <tspan x="65" y="295">adipiscing elit, sed do eiusmod tempor</tspan>
      <tspan x="65" y="324">incididunt ut labore et dolore magna aliqua.</tspan>
    </text>
    <text class="body-text" font-size="22">
      <tspan x="65" y="373">Lorem ipsum dolor sit amet, consectetur</tspan>
      <tspan x="65" y="402">adipiscing elit, sed do eiusmod tempor incididunt</tspan>
      <tspan x="65" y="431">ut labore et dolore magna aliqua. Quis ipsum</tspan>
      <tspan x="65" y="460">suspendisse ultrices gravida. Risus commodo</tspan>
      <tspan x="65" y="489">viverra maecenas accumsan lacus vel facilisis.</tspan>
    </text>
  </svg>

  <!-- Content slide B -->
  <svg class="slide slide--content-b" viewBox="0 0 1107 623" xmlns="http://www.w3.org/2000/svg">
    <defs>
      <linearGradient id="meeting-tone" x1="0" y1="0" x2="0" y2="1">
        <stop offset="0" stop-color="#4a4f63"/>
        <stop offset="0.55" stop-color="#2a2a30"/>
        <stop offset="1" stop-color="#5a5650"/>
      </linearGradient>
    </defs>
    <rect width="1107" height="623" fill="var(--paper)"/>
    <path class="shape-purple" d="M0,0 L490,0 C500,40 500,90 480,130 L480,430 C440,450 380,470 360,520 C380,560 395,600 390,623 L0,623 Z"/>
    <path class="shape-green" d="M910,0 C905,60 930,130 990,170 C1040,195 1080,180 1107,160 L1107,0 Z"/>
    <rect class="photo-frame--blue" x="46" y="93" width="433" height="354" rx="16" fill="url(#meeting-tone)" stroke-width="8" role="img" aria-label="Photo of a team meeting around a table in front of a data screen"/>
    <circle class="shape-green" cx="361" cy="478" r="54"/>
    <text class="caps-title caps-title--ink" x="541" y="169" font-size="62">SLIDE</text>
    <text class="caps-title caps-title--ink" x="541" y="228" font-size="62">HEADING</text>
    <text class="lead-text" font-size="23">
      <tspan x="548" y="273">Lorem ipsum dolor sit amet, consectetur</tspan>
      <tspan x="548" y="302">adipiscing elit, sed do eiusmod tempor</tspan>
      <tspan x="548" y="331">incididunt ut labore et dolore magna aliqua.</tspan>
    </text>
    <text class="body-text" font-size="22">
      <tspan x="548" y="377">Lorem ipsum dolor sit amet, consectetur</tspan>
      <tspan x="548" y="406">adipiscing elit, sed do eiusmod tempor incididunt</tspan>
      <tspan x="548" y="435">ut labore et dolore magna aliqua. Quis ipsum</tspan>
      <tspan x="548" y="464">suspendisse ultrices gravida. Risus commodo</tspan>
      <tspan x="548" y="493">viverra maecenas accumsan lacus vel facilisis.</tspan>
    </text>
  </svg>

</main>
</body>
</html>
```